Landing page in the senior sector

We need a landing page for families looking for retirement homes for their parent. The target is rather old (50-60 years old). The mandatory fields are Name, Email, Phone. The optional fields are budget, research zipcode, Emergency (,,). It is important to note that this is a free service that we offer to families in research. It should be noted that they are often in distress and repulsive. Need a mobile landing We need a landing page to recruit families looking for retirement homes for their parent. The target is rather old (50-60 years old). Required fields are Name, Email, Phone. The optional fields (they may not appear at all) are Budget, Search CP, Emergency (,,). It is important to mention that this is a free service that we offer to families in search. It should be noted that they are often in distress and that asking them for input may let tel may seem repulsive. Also need a mobile version

Target Market(s)

rather old (50-60 years old) / rather old (50-60 years old)

Coding

Coded - Design and coding required

Number of Pages Required

2 page

Font styles to use
Sans Serif

Colors

Designer to choose colors to be used in the design.

Requirements
Must have
• - A form with the 3 mandatory fields / A form with the 3 mandatory fields - Optimized for conversion / Optimized for conversion

```html
<!DOCTYPE html>
<html lang="en">
<head>
<meta charset="utf-8">
<title>Silver Haven Care – Assisted Living</title>
<link href="https://fonts.googleapis.com/css2?family=Roboto:wght@300;400;500;700&family=Playfair+Display:wght@700&display=swap" rel="stylesheet">
<style>
  :root{
    --page-bg:#ffffff;
    --navy:#0d2a4a;
    --blue-top:#1a7ac7;
    --blue-bottom:#0c4f8f;
    --green:#a6c927;
    --white:#ffffff;
    --field-border:#cfd3d8;
    --muted:#6b6f75;
    --required:#e0262b;
  }
  *{box-sizing:border-box;margin:0;padding:0}
  html,body{width:1200px;height:1200px;overflow:hidden;background:var(--page-bg)}
  body{position:relative;font-family:'Roboto',Arial,sans-serif}
  .hero{position:absolute;left:0;top:303px;width:1200px;height:595px;overflow:hidden}
  .hero-photo{position:absolute;inset:0;
    background:
      linear-gradient(90deg,rgba(20,40,60,0) 60%,rgba(0,0,0,0) 100%),
      radial-gradient(ellipse at 8% 10%,#eef0d4 0%,rgba(238,240,212,0) 35%),
      radial-gradient(ellipse at 100% 5%,#f4f07a 0%,rgba(244,240,122,0) 40%),
      linear-gradient(180deg,#b9c59a 0%,#7f9a6e 35%,#4d6470 70%,#1f3040 100%);}
  .hero-photo::after{content:"";position:absolute;inset:0;
    background:linear-gradient(90deg,rgba(40,70,80,.25) 0%,rgba(60,90,90,.1) 50%,rgba(150,200,40,.45) 100%)}
  .brand{position:absolute;left:53px;top:340px;display:flex;align-items:center;gap:8px}
  .brand-mark{width:14px;height:14px;background:var(--navy)}
  .brand-name{font-weight:700;font-size:16px;color:var(--navy)}
  .hotline{position:absolute;left:915px;top:322px;display:flex;align-items:center;gap:12px}
  .hotline-icon{width:28px;height:28px}
  .hotline-number{font-size:24px;font-weight:500;color:var(--navy);letter-spacing:.5px}
  .intro{position:absolute;left:152px;top:574px;color:var(--white)}
  .intro-kicker{font-weight:700;font-size:16px;margin-left:5px}
  .intro-title{font-family:'Playfair Display',Georgia,serif;font-weight:700;font-size:55px;line-height:61px;margin-top:6px}
  .lead-card{position:absolute;left:735px;top:435px;width:313px;height:375px;background:var(--white);box-shadow:0 2px 8px rgba(0,0,0,.2)}
  .lead-head{height:82px;background:linear-gradient(180deg,var(--blue-top),var(--blue-bottom));color:var(--white);padding:17px 0 0 25px}
  .lead-head-question{font-weight:300;font-size:17px}
  .lead-head-cta{font-weight:700;font-size:22px;letter-spacing:1.6px;margin-top:2px}
  .field{position:absolute;left:17px;width:278px;height:42px;border:1px solid var(--field-border);box-shadow:inset 0 1px 2px rgba(0,0,0,.08);font-size:11px;color:#555;padding:0 13px;display:flex;align-items:center}
  .field::after{content:"*";position:absolute;right:-9px;top:-8px;color:var(--required);font-size:11px}
  .field-name{top:107px}.field-email{top:162px}.field-phone{top:219px}
  .form-note{position:absolute;left:20px;top:275px;font-size:10px;color:var(--muted)}
  .form-note span{color:var(--required)}
  .submit{position:absolute;left:17px;top:305px;width:278px;height:40px;background:var(--green);color:var(--white);border:0;font-family:'Roboto',Arial,sans-serif;font-weight:700;font-size:14px;letter-spacing:.5px}
</style>
</head>
<body>
  <section class="hero">
    <div class="hero-photo" role="img" aria-label="Photo of an elderly couple walking hand in hand along a sunny country path"></div>
  </section>

  <div class="brand">
    <span class="brand-mark"></span>
    <span class="brand-name">SILVER HAVEN CARE</span>
  </div>

  <div class="hotline">
    <svg class="hotline-icon" viewBox="0 0 28 28" aria-hidden="true">
      <circle cx="14" cy="14" r="14" fill="#0d2a4a"/>
      <rect x="10" y="7" width="8" height="14" rx="1.5" fill="none" stroke="#fff" stroke-width="1.4"/>
      <circle cx="14" cy="18.5" r=".9" fill="#fff"/>
    </svg>
    <span class="hotline-number">555-014-2270</span>
  </div>

  <div class="intro">
    <p class="intro-kicker">WE CAN HELP YOU TODAY</p>
    <h1 class="intro-title">Certified Care<br>for your Family</h1>
  </div>

  <form class="lead-card">
    <div class="lead-head">
      <p class="lead-head-question">Looking for assisted Living Home?</p>
      <p class="lead-head-cta">Reserve yours Today!</p>
    </div>
    <div class="field field-name">Enter your name</div>
    <div class="field field-email">Enter your email</div>
    <div class="field field-phone">Enter your phone</div>
    <p class="form-note"><span>*</span> marks are mandatory fields</p>
    <button class="submit" type="button">RESERVE TODAY!</button>
  </form>
</body>
</html>
```